LA's Newest HEMP Facial Oil and Body Oil Packaging Project

We need a packaging concept for a Hemp based facial oil and body oil. We need label design for the bottle and carton graphics. I am attaching a few reference photos. The target demographic is women between 17-35 year old. Products need to be able to stand out in crowded stores with clear calls to action.
1oz Dropper Bottle with Unit Carton - Hemp Facial Oil
4oz PET Bottle with Unit Carton - Hemp + Rose Facial Oil

```html
<!DOCTYPE html>
<html lang="en">
<head>
<meta charset="utf-8">
<title>Hemp Based Facial Oil – Carton and Bottle Label</title>
<link href="https://fonts.googleapis.com/css2?family=Oswald:wght@500;600&family=Open+Sans:wght@600&display=swap" rel="stylesheet">
<style>
  :root {
    --hemp-green: #4b7d46;
    --paper: #eef0f1;
    --bg-light: #e7e8ea;
    --bg-dark: #c4c6ca;
  }
  html, body {
    margin: 0;
    padding: 0;
    width: 1200px;
    height: 1200px;
    overflow: hidden;
  }
  body {
    background: radial-gradient(ellipse at 50% 55%, var(--bg-light) 0%, var(--bg-dark) 100%);
    position: relative;
    font-family: "Open Sans", sans-serif;
  }

  /* Unit carton front panel */
  .carton {
    position: absolute;
    left: 258px;
    top: 110px;
    width: 356px;
    height: 866px;
    background: var(--hemp-green);
    overflow: hidden;
  }
  .carton__rule {
    position: absolute;
    left: 0;
    width: 100%;
    height: 3px;
    background: var(--paper);
  }
  .carton__rule--top-a { top: 32px; }
  .carton__rule--top-b { top: 42px; }
  .carton__rule--bottom-a { top: 818px; }
  .carton__rule--bottom-b { top: 830px; }
  .carton__band {
    position: absolute;
    left: 0;
    top: 234px;
    width: 100%;
    height: 456px;
    background: var(--paper);
  }

  .product-name {
    position: absolute;
    left: 0;
    width: 100%;
    margin: 0;
    text-align: center;
    font-family: "Oswald", sans-serif;
    font-weight: 500;
    color: var(--hemp-green);
    line-height: 1;
    letter-spacing: 1px;
  }
  .product-type {
    position: absolute;
    left: 0;
    width: 100%;
    margin: 0;
    text-align: center;
    font-size: 11px;
    letter-spacing: 1px;
    color: var(--hemp-green);
    line-height: 1;
  }
  .carton .product-name { top: 256px; font-size: 34px; }
  .carton .product-type { top: 310px; }

  .carton__headline {
    position: absolute;
    margin: 0;
    font-family: "Oswald", sans-serif;
    font-weight: 600;
    color: var(--hemp-green);
    line-height: 1;
    white-space: nowrap;
    transform-origin: left top;
    -webkit-text-stroke: 6px var(--paper);
    paint-order: stroke fill;
  }
  .carton__headline--natural { top: 371px; left: 26px; font-size: 85px; -webkit-text-stroke: 0; }
  .carton__headline--skin { top: 459px; left: -4px; font-size: 145px; transform: scaleX(1.4); }
  .carton__headline--care { top: 622px; left: -2px; font-size: 155px; transform: scaleX(1.07); }

  /* Dropper bottle label, laid flat */
  .bottle-label {
    position: absolute;
    left: 632px;
    top: 712px;
    width: 280px;
    height: 216px;
    background: var(--paper);
    box-shadow: inset 0 0 0 2px var(--hemp-green);
  }
  .bottle-label .product-name { top: 140px; font-size: 34px; }
  .bottle-label .product-type { top: 198px; }
</style>
</head>
<body>
  <section class="carton" aria-label="Unit carton front">
    <div class="carton__rule carton__rule--top-a"></div>
    <div class="carton__rule carton__rule--top-b"></div>
    <div class="carton__band"></div>

    <p class="product-name">HEMP BASED</p>
    <p class="product-type">FACIAL OIL</p>

    <p class="carton__headline carton__headline--natural">NATURAL</p>
    <p class="carton__headline carton__headline--skin">SKIN</p>
    <p class="carton__headline carton__headline--care">CARE</p>

    <div class="carton__rule carton__rule--bottom-a"></div>
    <div class="carton__rule carton__rule--bottom-b"></div>
  </section>

  <section class="bottle-label" aria-label="Dropper bottle label">
    <p class="product-name">HEMP BASED</p>
    <p class="product-type">FACIAL OIL</p>
  </section>
</body>
</html>
```